Design business card using existing logo.

PLEASE DO NOT USE "RED WHITE & BLACK" color combo! Thank you.

Try different color combos such as:
- Vintage colors like brown, orange, gold, blue (not all together but a combo of 1 or 3
- Blue, w/ grey, or silver or white, Blue monochromatic can work as well.
- Use monochromatic variations on back (just an idea)

- Include full name, "Quillmarsh Records" on at least one side.

Target Market(s)

Teens

Industry/Entity Type

Business

Colors
3277b5
ffc214
f04a50
f78f20

```html
<!DOCTYPE html>
<html lang="en">
<head>
<meta charset="utf-8">
<title>Quillmarsh Records – Business Card</title>
<link rel="stylesheet" href="https://fonts.googleapis.com/css2?family=Montserrat:wght@600&family=Special+Elite&display=swap">
<style>
  :root {
    --backdrop: #ece8e3;
    --card-orange: #f7941d;
    --card-black: #050505;
    --ink-dark: #2a2a2a;
    --stamp-red: #e8474f;
    --dot-orange: #f78f20;
    --dot-dark: #1c1c1c;
  }
  html, body {
    margin: 0;
    width: 1200px;
    height: 891px;
    overflow: hidden;
    background: var(--backdrop);
  }
  .canvas {
    position: relative;
    width: 1200px;
    height: 891px;
  }
  .card {
    position: absolute;
    top: 302px;
    width: 500px;
    height: 286px;
    overflow: hidden;
    box-shadow: 0 8px 24px rgba(0,0,0,0.18);
  }
  .card--front {
    left: 70px;
    background: var(--card-orange);
  }
  .card--back {
    left: 630px;
    background: var(--card-black);
  }
  .halftone {
    position: absolute;
    border-radius: 50%;
  }
  .card--front .halftone {
    left: 110px;
    top: -20px;
    width: 330px;
    height: 330px;
    background: radial-gradient(circle, rgba(28,28,28,0.05) 20%, rgba(28,28,28,0.28) 55%, rgba(28,28,28,0) 72%);
  }
  .card--back .halftone {
    left: 70px;
    top: -40px;
    width: 380px;
    height: 370px;
    background: radial-gradient(circle, rgba(247,143,32,0.15) 15%, rgba(247,143,32,0.55) 50%, rgba(247,143,32,0) 72%);
  }
  .brand {
    position: absolute;
    left: 0;
    top: 0;
    width: 100%;
    height: 100%;
  }
  .brand__mark {
    position: absolute;
    left: 228px;
    top: 52px;
    width: 100px;
    height: 100px;
    border-radius: 50%;
    background: var(--ink-dark);
  }
  .brand__name {
    position: absolute;
    left: 70px;
    top: 170px;
    margin: 0;
    font-family: "Montserrat", sans-serif;
    font-weight: 600;
    font-size: 44px;
    letter-spacing: 1px;
    color: var(--ink-dark);
    text-transform: uppercase;
  }
  .stamp {
    position: absolute;
    left: 50%;
    top: 50%;
    margin: 0;
    transform: translate(-50%, -50%) rotate(22deg);
    padding: 2px 6px;
    border-top: 3px solid var(--stamp-red);
    border-bottom: 3px solid var(--stamp-red);
    font-family: "Special Elite", monospace;
    font-size: 34px;
    color: var(--stamp-red);
    white-space: nowrap;
    text-transform: uppercase;
    letter-spacing: 1px;
  }
</style>
</head>
<body>
  <main class="canvas">
    <section class="card card--front" aria-label="Card front">
      <div class="halftone" role="img" aria-label="Dark halftone dot pattern radiating from the centre"></div>
      <div class="brand">
        <span class="brand__mark"></span>
        <h1 class="brand__name">Quillmarsh</h1>
      </div>
    </section>
    <section class="card card--back" aria-label="Card back">
      <div class="halftone" role="img" aria-label="Orange halftone dot pattern radiating from the centre"></div>
      <p class="stamp">Quillmarsh Records</p>
    </section>
  </main>
</body>
</html>
```